Business Card Design Project

I need a business card designed that is clean, simple and elegant.
I am a fashion and advertising photographer based in Cape Town and Durban South Africa.
check out my website: www.brennowalsh.co.za for ideas
Updates
Hi all,
Thanks for your submissions so far!
Please note:
I want no more than than black, white and/or grey to be used.
I don't want any photos used.
I would like the card to be double sided.
I would like to continue the design similar to the past ones Ive used.
I hope this helps, please send me further questions should you have any.
many thanks!
Brenno
Hi,
Please have a look at the jpg I loaded(called inspiration) which is the direction or inspiration I am aiming at.
Also PLEASE remember NO PHOTOS to be included on the card
many thanks!!
Target Market(s)
You can look at my site to get a better understanding of the audience:
www.brennowalsh.co.za
Industry/Entity Type
Advertising
Requirements
Must have
- Clean design which can also be used for a watermark on photographs
perhaps black background with white text/grey
company called: Brenno Walsh Photography
Nice to have
- below I have added logos that I have used in the past.
Should not have
- pictures of cameras
tacky elements

```html
<!DOCTYPE html>
<html lang="en">
<head>
<meta charset="utf-8">
<title>Brenno Walsh Photography – Business Card</title>
<link rel="stylesheet" href="https://fonts.googleapis.com/css2?family=Archivo+Black&family=Arimo:wght@400&family=Oswald:wght@700&display=swap">
<style>
  :root {
    --board: #8e9b98;
    --card: #e6ebea;
    --card-shade: #d3dad8;
    --ink: #4f5857;
    --ink-soft: #6a7473;
    --label: #ffffff;
    --pattern-light: #e4e9e8;
    --pattern-dark: #cdd4d2;
  }
  * { margin: 0; padding: 0; box-sizing: border-box; }
  html, body { width: 1200px; height: 576px; overflow: hidden; }
  body { background: var(--board); position: relative; font-family: "Arimo", Arial, sans-serif; }

  .card {
    position: absolute;
    top: 106px;
    width: 510px;
    height: 296px;
    background: var(--card);
    overflow: hidden;
  }
  .card--front { left: 57px; }
  .card--back { left: 630px; }

  .front__name-under {
    position: absolute;
    left: 33px;
    top: 132px;
    font-family: "Archivo Black", "Arial Black", sans-serif;
    font-size: 21px;
    color: var(--ink);
    white-space: nowrap;
    z-index: 1;
  }
  .front__flap {
    position: absolute;
    inset: 0;
    z-index: 2;
    filter: drop-shadow(-8px 0 10px rgba(60, 70, 68, 0.45));
  }
  .front__divider {
    position: absolute;
    left: 285px;
    top: 0;
    width: 1px;
    height: 100%;
    background: var(--card-shade);
    z-index: 3;
  }
  .front__details { position: absolute; inset: 0; z-index: 4; }
  .front__name {
    position: absolute;
    left: 306px;
    top: 76px;
    font-family: "Archivo Black", "Arial Black", sans-serif;
    font-size: 21px;
    color: var(--ink);
    white-space: nowrap;
  }
  .front__phone-icon { position: absolute; left: 311px; top: 130px; width: 30px; height: 26px; }
  .front__phones {
    position: absolute;
    left: 358px;
    top: 130px;
    font-size: 13px;
    line-height: 16px;
    color: var(--ink-soft);
  }
  .front__web {
    position: absolute;
    left: 303px;
    top: 193px;
    font-size: 13px;
    color: var(--ink-soft);
    letter-spacing: 0.3px;
  }

  .back__pattern {
    position: absolute;
    inset: 0;
    background: radial-gradient(ellipse at 30% 45%, var(--pattern-dark) 0%, var(--pattern-light) 45%),
                radial-gradient(ellipse at 78% 55%, var(--pattern-dark) 0%, transparent 40%);
    background-blend-mode: multiply;
  }

  .side-label {
    position: absolute;
    top: 432px;
    font-family: "Oswald", "Impact", sans-serif;
    font-weight: 700;
    font-size: 42px;
    letter-spacing: 3px;
    color: var(--label);
  }
  .side-label--front { left: 60px; }
  .side-label--back { right: 60px; }
</style>
</head>
<body>
  <section class="card card--front">
    <div class="front__name-under">BRENNO WALSH</div>
    <svg class="front__flap" viewBox="0 0 510 296" width="510" height="296" aria-hidden="true">
      <path d="M228 0 H510 V296 H228 A68 148 0 0 1 228 0 Z" fill="var(--card)"/>
    </svg>
    <div class="front__divider"></div>
    <div class="front__details">
      <h1 class="front__name">BRENNO WALSH</h1>
      <svg class="front__phone-icon" viewBox="0 0 30 26" aria-hidden="true">
        <path d="M2 8 Q15 -1 28 8 L25 12 L20 10 L20 7 Q15 5 10 7 L10 10 L5 12 Z" fill="var(--ink-soft)"/>
        <path d="M8 13 L22 13 L27 24 L3 24 Z" fill="var(--ink-soft)"/>
        <circle cx="15" cy="18.5" r="3" fill="var(--card)"/>
      </svg>
      <p class="front__phones">+27 (0)82 555 0147<br>+27 (0)31 555 0263</p>
      <p class="front__web">WWW.BRENNOWALSH.CO.ZA</p>
    </div>
  </section>

  <section class="card card--back">
    <div class="back__pattern" role="img" aria-label="Decorative swirling pattern of small grey numerals spiralling across the card"></div>
  </section>

  <div class="side-label side-label--front">FRONT</div>
  <div class="side-label side-label--back">BACK</div>
</body>
</html>
```